BrickaFun Business Card

We need a business card design for our company. We sell construction-themed amusement rides for kids.

Contact Information for Business Card

Contact info on business card should include:
Dale Hurst
Co-Founder & COO
(833) 517-BRICKAF
Dale@brickafun.com
www.brickafun.com

```html
<!DOCTYPE html>
<html lang="en">
<head>
<meta charset="utf-8">
<title>BrickaFun Business Card</title>
<link rel="stylesheet" href="https://fonts.googleapis.com/css2?family=Exo+2:wght@400;700&family=Russo+One&display=swap">
<style>
  :root {
    --stage: #161616;
    --card-dark: #222222;
    --card-darker: #141414;
    --paper: #f2f2f2;
    --magenta: #d2149a;
    --violet: #9a3fa9;
    --orange: #f0753a;
    --text-light: #f4f4f4;
    --photo-warm: #e89a4c;
    --photo-sky: #e9c3a4;
  }
  * { margin: 0; padding: 0; box-sizing: border-box; }
  html, body { width: 1200px; height: 900px; overflow: hidden; }
  body {
    background: var(--stage);
    display: flex;
    flex-direction: column;
    align-items: center;
    justify-content: center;
    gap: 36px;
    font-family: "Exo 2", sans-serif;
  }
  .card {
    position: relative;
    width: 700px;
    height: 400px;
    border-radius: 28px;
    overflow: hidden;
    background: var(--card-dark);
    box-shadow: 0 14px 30px rgba(0,0,0,.55);
  }
  .card-art { position: absolute; inset: 0; width: 100%; height: 100%; }

  /* front */
  .crew-illustration {
    position: absolute;
    left: 150px; top: 18px;
    width: 250px; height: 165px;
    border-radius: 12px;
    background: radial-gradient(ellipse at 50% 35%, rgba(240,200,40,.55), rgba(60,60,70,.35) 70%, transparent);
  }
  .contact-list {
    position: absolute;
    left: 70px; top: 212px;
    list-style: none;
    color: var(--text-light);
    font-size: 21px;
    line-height: 32px;
    letter-spacing: .5px;
  }
  .contact-list li { display: flex; align-items: center; gap: 12px; }
  .contact-icon { width: 20px; height: 20px; flex: none; }
  .brand-mark {
    position: absolute;
    left: 440px; right: 28px; top: 122px;
    display: flex; align-items: center; justify-content: center; gap: 10px;
    color: var(--orange);
    font-weight: 700;
    font-size: 40px;
    line-height: 1;
    white-space: nowrap;
  }
  .brand-dot {
    width: 20px; height: 20px; border-radius: 50%;
    background: var(--orange);
    flex: none;
  }
  .person {
    position: absolute;
    right: 40px; top: 284px;
    text-align: right;
  }
  .person-name {
    font-family: "Russo One", sans-serif;
    color: var(--orange);
    font-size: 30px;
    line-height: 38px;
    letter-spacing: 2px;
  }
  .person-title {
    color: var(--text-light);
    font-size: 20px;
    line-height: 28px;
    letter-spacing: 1px;
  }

  /* back */
  .site-photo {
    position: absolute;
    inset: 0 0 auto 0;
    height: 175px;
    background: linear-gradient(180deg, var(--photo-sky), var(--photo-warm) 60%, #b9652c);
  }
  .back-brand {
    position: absolute;
    left: 0; right: 0; top: 215px;
    display: flex; justify-content: center; align-items: center; gap: 14px;
    color: var(--orange);
    font-weight: 700;
    font-size: 60px;
    line-height: 1;
    white-space: nowrap;
  }
  .back-brand .brand-dot { width: 26px; height: 26px; }
</style>
</head>
<body>

<section class="card card-front">
  <svg class="card-art" viewBox="0 0 700 400" aria-hidden="true">
    <defs>
      <linearGradient id="bandFront" x1="0" x2="1">
        <stop offset="0" stop-color="#d2149a"/>
        <stop offset="1" stop-color="#9a3fa9"/>
      </linearGradient>
    </defs>
    <rect width="700" height="400" fill="#222"/>
    <polygon points="470,0 700,0 700,400 330,400" fill="#f2f2f2"/>
    <polygon points="445,275 700,275 700,362 395,362 425,318" fill="#242424"/>
    <polygon points="0,190 410,190 445,262 410,335 0,335" fill="url(#bandFront)"/>
  </svg>

  <div class="crew-illustration" role="img" aria-label="Cartoon pair of construction workers in yellow hard hats"></div>

  <ul class="contact-list">
    <li>
      <svg class="contact-icon" viewBox="0 0 20 20"><circle cx="10" cy="10" r="9" fill="none" stroke="#fff" stroke-width="1.5"/><path d="M6 6c0 5 3 8 8 8l1-2-2-1-1 1c-2-1-3-2-4-4l1-1-1-2z" fill="#fff"/></svg>
      (833) 517-BRICKAF
    </li>
    <li>
      <svg class="contact-icon" viewBox="0 0 20 20"><circle cx="10" cy="10" r="9" fill="none" stroke="#fff" stroke-width="1.5"/><rect x="5" y="6.5" width="10" height="7" fill="none" stroke="#fff" stroke-width="1.3"/><path d="M5 6.5l5 4 5-4" fill="none" stroke="#fff" stroke-width="1.3"/></svg>
      Dale@brickafun.com
    </li>
    <li>
      <svg class="contact-icon" viewBox="0 0 20 20"><circle cx="10" cy="10" r="9" fill="none" stroke="#fff" stroke-width="1.5"/><ellipse cx="10" cy="10" rx="3.5" ry="7" fill="none" stroke="#fff" stroke-width="1.2"/><path d="M3 10h14" stroke="#fff" stroke-width="1.2"/></svg>
      www.brickafun.com
    </li>
  </ul>

  <div class="brand-mark"><span class="brand-dot"></span>BrickaFun</div>

  <div class="person">
    <p class="person-name">DALE HURST</p>
    <p class="person-title">Co-Founder &amp; COO</p>
  </div>
</section>

<section class="card card-back">
  <svg class="card-art" viewBox="0 0 700 400" aria-hidden="true">
    <defs>
      <linearGradient id="bandBack" x1="0" x2="1">
        <stop offset="0" stop-color="#d2149a"/>
        <stop offset="1" stop-color="#9a3fa9"/>
      </linearGradient>
    </defs>
    <rect width="700" height="400" fill="#1e1e1e"/>
    <rect y="330" width="700" height="70" fill="#141414"/>
    <polygon points="0,175 70,175 58,200 0,200" fill="#d2149a"/>
    <polygon points="330,295 700,295 700,330 330,330 350,312" fill="url(#bandBack)"/>
  </svg>
  <div class="site-photo" role="img" aria-label="Photo of orange excavator kiddie rides at a sunny amusement site"></div>
  <div class="back-brand"><span class="brand-dot"></span>BrickaFun</div>
</section>

</body>
</html>
```